Web Design for Rubbish Removal Company

I am looking for a custom web design that is clean and modern which also has a professional trustworthy feel to it.
The website is http://www.tidlowhaulage.com.au/ and need:
1 x Front Page
1 x Location Page
Please keep the green colour scheme as this is the corporate colours but would like to steer away from the black.
Industry/Entity Type
It Company
Number of Pages Required
2 page
Font styles to use
Sans Serif
Requirements
Must have
- Clean & Professional
- Keep green colour scheme
Should not have
- Steer away from black
- not look like a template

```html
<!DOCTYPE html>
<html lang="en">
<head>
<meta charset="utf-8">
<title>Tidlow Haulage – Rubbish Removal Sydney</title>
<link href="https://fonts.googleapis.com/css2?family=Roboto:wght@300;400;500;700;900&display=swap" rel="stylesheet">
<style>
:root{
  --green:#7cc242;
  --green-dark:#5fa52c;
  --green-band:#8bc850;
  --forest:#2f4526;
  --forest-deep:#243720;
  --ink:#333a30;
  --muted:#7a7f78;
  --line:#dcdfd9;
  --paper:#ffffff;
  --soft:#f4f5f3;
}
*{box-sizing:border-box;margin:0;padding:0}
html,body{width:1200px;height:2840px;overflow:hidden}
body{font-family:"Roboto",Arial,sans-serif;color:var(--ink);background:var(--paper);font-size:14px}
.wrap{width:1060px;margin:0 auto;position:relative}
a{color:inherit;text-decoration:none}

/* top bar */
.topbar{height:24px;background:var(--forest-deep);color:#d7e3cf;font-size:11px}
.topbar .wrap{display:flex;justify-content:space-between;align-items:center;height:24px}
.topbar .contact{display:flex;gap:24px}
.topbar .contact span{display:flex;align-items:center;gap:6px}

/* header */
.header{height:96px;border-bottom:1px solid var(--line)}
.header .wrap{display:flex;justify-content:space-between;align-items:center;height:96px}
.brand{display:flex;align-items:center;gap:10px;font-weight:900;font-size:26px;color:var(--forest);letter-spacing:.5px}
.brand-dot{width:20px;height:20px;background:var(--green)}
.nav{display:flex;gap:6px}
.nav a{font-size:12px;font-weight:500;padding:10px 16px;color:var(--ink);letter-spacing:.5px}
.nav a.active{background:var(--green);color:#fff}

/* hero */
.hero{height:440px;position:relative;background:linear-gradient(100deg,#c9d2cf 0%,#e7ebe8 45%,#d9dfdc 100%)}
.hero-photo{position:absolute;inset:0}
.hero-perks{position:absolute;left:500px;top:110px;list-style:none}
.hero-perks li{font-size:19px;font-weight:900;color:var(--forest);font-style:normal;text-transform:uppercase;margin-bottom:10px;display:flex;align-items:center;gap:10px}
.hero-badge{position:absolute;right:90px;top:40px;width:150px;height:150px;border-radius:50%;background:#d8b23a}

/* tagline band */
.band{height:120px;background:var(--green-band)}
.band .wrap{display:flex;justify-content:space-between;align-items:center;height:120px}
.band h1{color:#fff;font-size:28px;font-weight:500}
.btn-ghost{border:2px solid #fff;color:#fff;font-size:15px;padding:10px 26px;border-radius:4px}

/* section headings */
.sec-head{text-align:center}
.sec-head .kicker{font-size:17px;color:var(--muted);font-weight:300}
.sec-head h2{font-size:28px;font-weight:700;color:var(--ink);text-transform:uppercase;margin-top:2px}
.sec-head .rule{width:60px;height:3px;background:var(--green);margin:10px auto 0}

/* services */
.services{height:460px;padding-top:40px}
.service-grid{display:flex;gap:30px;margin-top:26px}
.service-card{flex:1}
.service-img{height:180px;background:linear-gradient(135deg,#5a5e52,#3f4a3a)}
.service-img.office{background:linear-gradient(135deg,#b9bdb6,#8e9589)}
.service-img.build{background:linear-gradient(135deg,#8e8a80,#5f5b52)}
.service-card h3{font-size:18px;font-weight:500;margin:14px 0 6px}
.service-card p{font-size:12px;line-height:1.55;color:var(--muted)}
.more{display:inline-block;margin-top:8px;font-size:11px;font-weight:700;color:var(--green)}
.btn-solid{display:block;width:110px;margin:22px auto 0;background:var(--green);color:#fff;font-size:12px;font-weight:700;text-align:center;padding:10px 0;border-radius:3px}

/* news */
.news{height:620px;background:var(--green);padding-top:40px}
.news .sec-head .kicker{color:#eaf5df}
.news .sec-head h2{color:var(--forest)}
.news .sec-head .rule{background:#fff}
.news-grid{display:flex;gap:30px;margin-top:30px}
.news-feature{width:300px}
.news-img{height:150px;background:linear-gradient(135deg,#6d6b60,#4b4d44)}
.news-img.tidy{background:linear-gradient(135deg,#a7a49b,#6e6b64)}
.news-feature h3{font-size:18px;font-weight:500;color:#fff;margin:16px 0 8px;line-height:1.3}
.news-feature p{font-size:12px;line-height:1.55;color:#eef7e6}
.news-list{flex:1}
.news-list li{list-style:none;font-size:18px;font-weight:500;color:#fff;padding:18px 0;border-bottom:1px solid rgba(255,255,255,.5);line-height:1.35}
.news-list li:first-child{padding-top:0}
.news-list .more{color:#fff;font-size:15px;float:right;margin-top:18px}

/* booking */
.booking{height:460px;padding-top:40px}
.booking-body{display:flex;gap:30px;margin-top:30px}
.form{flex:1;display:grid;grid-template-columns:1fr 1fr;gap:18px 30px}
.field label{display:block;font-size:12px;font-weight:500;margin-bottom:6px}
.field .box{height:32px;border:1px solid var(--line);background:#fff;font-size:11px;color:var(--muted);padding:0 10px;display:flex;align-items:center;justify-content:space-between}
.field.msg{grid-column:span 2}
.field.msg .box{height:96px}
.side{width:333px;display:flex;flex-direction:column;gap:18px}
.fast{background:var(--green);color:#fff;text-align:center;padding:28px 20px;flex:1;display:flex;flex-direction:column;justify-content:center}
.fast h4{font-size:18px;font-weight:500}
.fast p{font-size:13px;margin:6px 0 14px}
.fast .phone{font-size:26px;font-weight:700;display:flex;align-items:center;justify-content:center;gap:10px}

/* testimonial */
.testimonial{height:280px;background:var(--soft);padding-top:40px}
.quote{display:flex;gap:20px}
.quote-mark{font-size:70px;line-height:.8;color:#b9beb5;font-weight:900}
.quote p{font-size:18px;font-weight:500;line-height:1.5;color:var(--ink);max-width:860px}
.author{display:flex;align-items:center;gap:16px;margin:26px 0 0 60px}
.avatar{width:64px;height:64px;border-radius:50%;background:#c7cbc3}
.author strong{display:block;font-size:15px}
.author span{font-size:12px;color:var(--green)}
.arrows{position:absolute;right:0;top:80px;display:flex;gap:6px}
.arrows span{width:28px;height:28px;background:#d3d7cf;display:flex;align-items:center;justify-content:center}

/* footer */
.footer{height:300px;background:var(--forest);color:#dfe8d9;padding-top:40px}
.footer .wrap{display:flex;gap:40px}
.fcol{flex:1}
.fcol h5{font-size:13px;font-weight:700;color:#fff;text-transform:uppercase;margin-bottom:16px}
.fcol li{list-style:none;font-size:12px;line-height:2}
.fcol .ci{display:flex;align-items:center;gap:8px;margin-bottom:12px;font-size:12px}
.social{display:flex;gap:12px}
.social span{width:20px;height:20px;border-radius:50%;background:#9fc27f}
.copy{height:40px;background:var(--forest-deep);color:#a8b8a0;font-size:11px;display:flex;align-items:center;justify-content:center}
</style>
</head>
<body>

<div class="topbar">
  <div class="wrap">
    <span>Monday through to Sunday, All day</span>
    <div class="contact">
      <span><svg width="10" height="10" viewBox="0 0 24 24"><path fill="#9fd36a" d="M6.6 10.8a15 15 0 0 0 6.6 6.6l2.2-2.2c.3-.3.7-.4 1-.2 1.1.4 2.3.6 3.6.6.6 0 1 .4 1 1V20c0 .6-.4 1-1 1A17 17 0 0 1 3 4c0-.6.4-1 1-1h3.5c.6 0 1 .4 1 1 0 1.3.2 2.5.6 3.6.1.3 0 .7-.2 1z"/></svg>+0400 555 018</span>
      <span><svg width="11" height="9" viewBox="0 0 24 18"><rect x="1" y="1" width="22" height="16" fill="none" stroke="#9fd36a" stroke-width="2"/><path d="M1 1l11 9 11-9" fill="none" stroke="#9fd36a" stroke-width="2"/></svg>hello@tidlowhaulage.com.au</span>
    </div>
  </div>
</div>

<header class="header">
  <div class="wrap">
    <a class="brand" href="http://www.tidlowhaulage.com.au/"><span class="brand-dot"></span>TIDLOW HAULAGE</a>
    <nav class="nav">
      <a class="active" href="#">HOME</a><a href="#">ABOUT</a><a href="#">SERVICES</a><a href="#">GALLERY</a><a href="#">FAQS</a><a href="#">BLOG</a><a href="#">CONTACT</a>
    </nav>
  </div>
</header>

<section class="hero">
  <div class="hero-photo" role="img" aria-label="Photo of a white rubbish removal truck on the left and a smiling worker giving a thumbs up on the right"></div>
  <ul class="hero-perks">
    <li><svg width="18" height="18" viewBox="0 0 24 24"><path d="M4 12l5 5L20 6" fill="none" stroke="#5fa52c" stroke-width="4"/></svg>Free Quote</li>
    <li><svg width="18" height="18" viewBox="0 0 24 24"><path d="M4 12l5 5L20 6" fill="none" stroke="#5fa52c" stroke-width="4"/></svg>Cheapest Price</li>
    <li><svg width="18" height="18" viewBox="0 0 24 24"><path d="M4 12l5 5L20 6" fill="none" stroke="#5fa52c" stroke-width="4"/></svg>Always On-Time</li>
    <li><svg width="18" height="18" viewBox="0 0 24 24"><path d="M4 12l5 5L20 6" fill="none" stroke="#5fa52c" stroke-width="4"/></svg>Same-Day</li>
    <li><svg width="18" height="18" viewBox="0 0 24 24"><path d="M4 12l5 5L20 6" fill="none" stroke="#5fa52c" stroke-width="4"/></svg>10+ Years Exp</li>
  </ul>
  <div class="hero-badge" role="img" aria-label="Guarantee seal"></div>
</section>

<section class="band">
  <div class="wrap">
    <h1>Sydney's Cheapest Rubbish Removal Services</h1>
    <a class="btn-ghost" href="#">Send A Quote</a>
  </div>
</section>

<section class="services">
  <div class="wrap">
    <div class="sec-head">
      <div class="kicker">Our Services</div>
      <h2>High Quality Services</h2>
      <div class="rule"></div>
    </div>
    <div class="service-grid">
      <article class="service-card">
        <div class="service-img" role="img" aria-label="Photo of bagged household rubbish piled up"></div>
        <h3>Household Rubbish Removals</h3>
        <p>Do you have rubbish slowly building up at home? Quickly clear out space with our friendly team and get your household back to tidy, calm order today.</p>
        <a class="more" href="#">READ MORE »</a>
      </article>
      <article class="service-card">
        <div class="service-img office" role="img" aria-label="Photo of office chairs and desks ready for removal"></div>
        <h3>Office Rubbish Removals</h3>
        <p>Most companies are busy running their business and have little time for clear outs. We make office rubbish removal quick, quiet and fully sorted.</p>
        <a class="more" href="#">READ MORE »</a>
      </article>
      <article class="service-card">
        <div class="service-img build" role="img" aria-label="Photo of construction and demolition debris"></div>
        <h3>Construction Rubbish Removals</h3>
        <p>Construction and demolition waste usually consists of heavy bricks, timber, concrete and plaster. We haul it away safely, on time and at fair rates.</p>
        <a class="more" href="#">READ MORE »</a>
      </article>
    </div>
    <a class="btn-solid" href="#">LOAD MORE</a>
  </div>
</section>

<section class="news">
  <div class="wrap">
    <div class="sec-head">
      <div class="kicker">News</div>
      <h2>Total Updates From The Blog</h2>
      <div class="rule"></div>
    </div>
    <div class="news-grid">
      <article class="news-feature">
        <div class="news-img" role="img" aria-label="Photo of a cluttered yard during summer clean-up"></div>
        <h3>How to work safely in the summer heat</h3>
        <p>As the summer heat arrives, plan your outdoor jobs for the cooler hours, drink plenty of water and book bulky pickups early in the morning.</p>
      </article>
      <article class="news-feature">
        <div class="news-img tidy" role="img" aria-label="Photo of an office being cleared of clutter"></div>
        <h3>Top 8 Tips On How To Keep Your Office Cline</h3>
        <p>A clean desk helps a clear mind. Sort papers weekly, recycle old devices and keep shared spaces free of clutter so your team can focus.</p>
      </article>
      <ul class="news-list">
        <li>3 Tips On What Not To Do With Your Rubbish</li>
        <li>How To Choose The Right Rubbish Removal company</li>
        <li>Importance Of Keeping Your Home Organised &amp; Neat</li>
        <a class="more" href="#">MORE NEWS »</a>
      </ul>
    </div>
  </div>
</section>

<section class="booking">
  <div class="wrap">
    <div class="sec-head">
      <div class="kicker">We Provide Annual</div>
      <h2>Service Booking</h2>
      <div class="rule"></div>
    </div>
    <div class="booking-body">
      <div class="form">
        <div class="field"><label>Your Name</label><div class="box"></div></div>
        <div class="field"><label>Your Email</label><div class="box"></div></div>
        <div class="field"><label>Address</label><div class="box"></div></div>
        <div class="field"><label>Choose a Service</label><div class="box">Choose a service <span>▾</span></div></div>
        <div class="field msg"><label>Message</label><div class="box"></div></div>
      </div>
      <div class="side">
        <div class="field"><label>Your Phone Number</label><div class="box"></div></div>
        <div class="field"><label>Payment Plan</label><div class="box">Payment Plan <span>▾</span></div></div>
        <div class="fast">
          <h4>Fast Booking</h4>
          <p>Call us for booking information</p>
          <div class="phone"><svg width="22" height="22" viewBox="0 0 24 24"><path fill="#fff" d="M6.6 10.8a15 15 0 0 0 6.6 6.6l2.2-2.2c.3-.3.7-.4 1-.2 1.1.4 2.3.6 3.6.6.6 0 1 .4 1 1V20c0 .6-.4 1-1 1A17 17 0 0 1 3 4c0-.6.4-1 1-1h3.5c.6 0 1 .4 1 1 0 1.3.2 2.5.6 3.6.1.3 0 .7-.2 1z"/></svg>+0400 555 018</div>
        </div>
      </div>
    </div>
  </div>
</section>

<section class="testimonial">
  <div class="wrap">
    <div class="quote">
      <div class="quote-mark">“</div>
      <p>Excellent service; quote given on the spot for major clean up of household throw outs. The team provides quick, efficient and courteous removal! Very satisfied customer.</p>
    </div>
    <div class="author">
      <div class="avatar" role="img" aria-label="Customer portrait"></div>
      <div><strong>Marcus Delaney</strong><span>Coogee</span></div>
    </div>
    <div class="arrows">
      <span><svg width="8" height="12" viewBox="0 0 8 12"><path d="M6 1L1 6l5 5" fill="none" stroke="#fff" stroke-width="2"/></svg></span>
      <span><svg width="8" height="12" viewBox="0 0 8 12"><path d="M2 1l5 5-5 5" fill="none" stroke="#fff" stroke-width="2"/></svg></span>
    </div>
  </div>
</section>

<footer class="footer">
  <div class="wrap">
    <div class="fcol">
      <h5>Contacts</h5>
      <div class="ci"><svg width="12" height="14" viewBox="0 0 24 28"><path fill="#9fd36a" d="M12 0a10 10 0 0 0-10 10c0 8 10 18 10 18s10-10 10-18A10 10 0 0 0 12 0zm0 14a4 4 0 1 1 0-8 4 4 0 0 1 0 8z"/></svg>Australia Sydney</div>
      <div class="ci"><svg width="12" height="12" viewBox="0 0 24 24"><path fill="#9fd36a" d="M6.6 10.8a15 15 0 0 0 6.6 6.6l2.2-2.2c.3-.3.7-.4 1-.2 1.1.4 2.3.6 3.6.6.6 0 1 .4 1 1V20c0 .6-.4 1-1 1A17 17 0 0 1 3 4c0-.6.4-1 1-1h3.5c.6 0 1 .4 1 1 0 1.3.2 2.5.6 3.6.1.3 0 .7-.2 1z"/></svg>+0400 555 018</div>
      <div class="ci"><svg width="12" height="10" viewBox="0 0 24 18"><rect x="1" y="1" width="22" height="16" fill="none" stroke="#9fd36a" stroke-width="2"/><path d="M1 1l11 9 11-9" fill="none" stroke="#9fd36a" stroke-width="2"/></svg>hello@tidlowhaulage.com.au</div>
    </div>
    <div class="fcol">
      <h5>Quick Links</h5>
      <ul><li>Home</li><li>About</li><li>Service</li><li>Gallery</li><li>Faqs</li><li>Blog</li><li>Contact us</li></ul>
    </div>
    <div class="fcol">
      <h5>Services</h5>
      <ul><li>Residential homes</li><li>Eateries &amp; retail stores</li><li>Office/commercial buildings</li><li>Construction/demolition sites</li><li>Uncovered estates</li></ul>
    </div>
    <div class="fcol">
      <h5>Follow Us</h5>
      <div class="social"><span></span><span></span><span></span><span></span><span></span><span></span></div>
    </div>
  </div>
</footer>
<div class="copy">Copyright © Tidlow Haulage. All Rights Reserved.</div>

</body>
</html>
```